New business card for civil engineering company - "Keystone Audit"

We need a business card designed for our new structural engineering company.

The company name is "Keystone Audit" logo files attached.

We would like the following:
* Two-sided card
* Simple design

Information to be placed on the card:
Name - Marcus Dellow
Job Title - Director / Structural Engineer
Credentials - BEng(Hons), CPEng, CMengNZ, IntPE(NZ)
Email - marcus.dellow@keystoneaudit.co.nz
mobile - 0219364058
website - www.keystoneaudit.co.nz

```html
<!DOCTYPE html>
<html lang="en">
<head>
<meta charset="utf-8">
<title>Keystone Audit – Business Card</title>
<link href="https://fonts.googleapis.com/css2?family=Lato:wght@400;700;900&display=swap" rel="stylesheet">
<style>
  :root {
    --page-bg: #e6e6e4;
    --card-light-top: #e2e2e2;
    --card-light-bottom: #f7f7f7;
    --card-dark: #000000;
    --edge-navy: #0d3d75;
    --ink: #2b2b2b;
    --ink-soft: #4a4a4a;
    --icon-navy: #123f73;
    --brand-blue: #3b8fd0;
    --brand-light: #f2f2f2;
    --brand-grey: #9a9a9a;
  }
  * { margin: 0; padding: 0; box-sizing: border-box; }
  html, body {
    width: 1200px; height: 900px; overflow: hidden;
    background: var(--page-bg);
    font-family: "Lato", Arial, sans-serif;
  }
  .canvas {
    width: 1200px; height: 900px;
    display: flex; flex-direction: column; align-items: center; justify-content: center;
    gap: 48px;
  }
  .card {
    position: relative;
    width: 665px; height: 380px;
    border-bottom: 6px solid var(--edge-navy);
    box-shadow: 0 10px 24px rgba(0,0,0,0.22);
  }
  .card--front {
    background: linear-gradient(180deg, var(--card-light-top), var(--card-light-bottom));
  }
  .card--back {
    background: var(--card-dark);
    display: flex; align-items: center; justify-content: center;
  }

  /* brand lockup */
  .brand { display: flex; flex-direction: column; align-items: flex-start; }
  .brand__row { display: flex; align-items: center; gap: 10px; }
  .brand__square { width: 16px; height: 16px; background: var(--brand-blue); }
  .brand__name { font-weight: 700; letter-spacing: 0.06em; text-transform: uppercase; }
  .brand__tagline { text-transform: uppercase; letter-spacing: 0.26em; margin-top: 6px; }

  .card--front .brand { position: absolute; left: 70px; top: 230px; }
  .card--front .brand__name { font-size: 24px; color: var(--ink); }
  .card--front .brand__tagline { font-size: 10px; color: var(--ink-soft); }

  .card--back .brand { align-items: center; }
  .card--back .brand__square { background: var(--brand-grey); }
  .card--back .brand__name { font-size: 34px; color: var(--brand-light); }
  .card--back .brand__tagline { font-size: 13px; color: var(--brand-light); margin-top: 8px; }

  /* details */
  .details { position: absolute; left: 330px; top: 78px; color: var(--ink); }
  .details__name { font-size: 30px; letter-spacing: 0.01em; text-transform: uppercase; line-height: 1; }
  .details__name strong { font-weight: 900; }
  .details__name span { font-weight: 400; }
  .details__role, .details__creds { font-size: 14px; color: var(--ink-soft); margin-top: 6px; }
  .details__creds { margin-top: 3px; }
  .contact { list-style: none; margin-top: 22px; }
  .contact__item { display: flex; align-items: center; gap: 14px; font-size: 14px; color: var(--ink-soft); margin-bottom: 9px; }
  .contact__icon { width: 18px; height: 18px; flex: none; }
</style>
</head>
<body>
<main class="canvas">
  <section class="card card--front">
    <div class="brand">
      <div class="brand__row">
        <span class="brand__square"></span>
        <span class="brand__name">Keystone Audit</span>
      </div>
      <span class="brand__tagline">Peer Review Specialists</span>
    </div>

    <div class="details">
      <h1 class="details__name"><strong>Marcus</strong> <span>Dellow</span></h1>
      <p class="details__role">Director / Structural Engineer</p>
      <p class="details__creds">BEng(Hons), CPEng, CMengNZ, IntPE(NZ)</p>
      <ul class="contact">
        <li class="contact__item">
          <svg class="contact__icon" viewBox="0 0 24 24" aria-hidden="true"><path fill="var(--icon-navy)" d="M6.6 10.8a15.1 15.1 0 0 0 6.6 6.6l2.2-2.2c.3-.3.7-.4 1-.2 1.1.4 2.3.6 3.6.6.6 0 1 .4 1 1V20c0 .6-.4 1-1 1A17 17 0 0 1 3 4c0-.6.4-1 1-1h3.5c.6 0 1 .4 1 1 0 1.3.2 2.5.6 3.6.1.3 0 .7-.2 1z"/></svg>
          <span>021 936 4058</span>
        </li>
        <li class="contact__item">
          <svg class="contact__icon" viewBox="0 0 24 24" aria-hidden="true"><rect x="2" y="5" width="20" height="14" fill="var(--icon-navy)"/><path d="M2 5l10 8 10-8" fill="none" stroke="#fff" stroke-width="1.5"/></svg>
          <span>marcus.dellow@keystoneaudit.co.nz</span>
        </li>
        <li class="contact__item">
          <svg class="contact__icon" viewBox="0 0 24 24" aria-hidden="true"><g fill="none" stroke="var(--icon-navy)" stroke-width="1.8"><circle cx="12" cy="12" r="9"/><ellipse cx="12" cy="12" rx="4" ry="9"/><path d="M3 12h18M5 7.5h14M5 16.5h14"/></g></svg>
          <span>www.keystoneaudit.co.nz</span>
        </li>
      </ul>
    </div>
  </section>

  <section class="card card--back">
    <div class="brand">
      <div class="brand__row">
        <span class="brand__square"></span>
        <span class="brand__name">Keystone Audit</span>
      </div>
      <span class="brand__tagline">Peer Review Specialists</span>
    </div>
  </section>
</main>
</body>
</html>
```